Flyer design for the Harvest Lantern Summit 2019 (HALSUM)

Design a flyer for our annual conference with basic information about the conference: conference logo and year, Conference name: Harvest Lantern Summit Location: Talbot Community Center (Downtown Portland)482 Wexley Street, Portland, ME 04109, Date: August 8th, 9th, 10th and 11th, 2019Start time 7:00PMI would like the following three words added to the flyer. These words describe the vision of the conference: Prophetic, Fire, Overflow,

Contact info:
Website: www.vostel.org
Phone: 207 555 3184
Email: contact@meadowcrest.org

Target Market(s)

Young adults living in the United States

Industry/Entity Type

Religious

Font styles to use
Sans Serif

Colors

Designer to choose colors to be used in the design.

Requirements
Must have
• HALSUM must logo standout, the reader should be able to take a quick look and find key info,
Should not have
• Cross image, church image

```html
<!DOCTYPE html>
<html lang="en">
<head>
<meta charset="utf-8">
<title>Harvest Lantern Summit 2019</title>
<link rel="stylesheet" href="https://fonts.googleapis.com/css2?family=Barlow+Semi+Condensed:wght@600&family=Montserrat:wght@600;700&display=swap">
<style>
  :root {
    --navy: #0b5896;
    --blue: #1673bd;
    --orange: #f7941e;
    --cream: #fdf1e4;
    --sky-light: #d9eef8;
    --sky: #a9d8f0;
    --sky-deep: #86c6e8;
    --deep-blue: #0d5a95;
  }
  * { margin: 0; padding: 0; box-sizing: border-box; }
  html, body { width: 913px; height: 1200px; overflow: hidden; }
  body { font-family: "Montserrat", sans-serif; color: var(--navy); }
  .flyer {
    position: relative; width: 913px; height: 1200px; overflow: hidden;
    background: linear-gradient(180deg, var(--cream) 0%, #f1f3ef 30%, var(--sky-light) 52%, var(--sky) 80%, var(--sky-deep) 100%);
  }
  .flyer > * { position: absolute; }
  .brand { left: 0; width: 913px; top: 58px; text-align: center; }
  .brand-name { font-size: 56px; font-weight: 700; color: var(--blue); letter-spacing: 2px; line-height: 1; }
  .brand-year {
    display: flex; align-items: center; justify-content: center; gap: 10px;
    margin-top: 4px; font-size: 24px; font-weight: 700; color: var(--orange); letter-spacing: 12px; line-height: 1;
  }
  .brand-year::before, .brand-year::after { content: ""; width: 68px; height: 2px; background: var(--orange); }
  .brand-year::after { margin-left: -12px; }
  .title {
    left: 0; width: 913px; top: 176px; text-align: center;
    font-family: "Barlow Semi Condensed", sans-serif; font-weight: 600;
    font-size: 86px; line-height: 70px; letter-spacing: 2px; color: var(--navy);
  }
  .date-label { left: 104px; top: 374px; font-size: 48px; font-weight: 700; color: var(--blue); }
  .date-label span { font-size: 34px; margin-left: 8px; }
  .date-lines { left: 313px; top: 381px; font-size: 33px; font-weight: 700; line-height: 49px; }
  .date-lines .second { padding-left: 97px; }
  .accent { color: var(--orange); }
  .start-time {
    left: 146px; top: 502px; width: 638px; height: 77px;
    border: 2.5px solid var(--blue); border-radius: 40px;
    display: flex; align-items: center; justify-content: center;
    font-size: 40px; font-weight: 700; letter-spacing: 1px;
  }
  .vision { font-size: 41px; font-weight: 700; line-height: 1; display: flex; align-items: center; gap: 18px; }
  .vision::before { content: ""; width: 24px; height: 24px; border-radius: 50%; background: var(--orange); }
  .vision-prophetic { left: 73px; top: 625px; }
  .vision-overflow { left: 460px; top: 625px; }
  .vision-fire { left: 362px; top: 692px; }
  .flame-area {
    left: 0; top: 690px; width: 340px; height: 510px;
    background: radial-gradient(ellipse at 55% 70%, var(--orange) 0%, rgba(247,148,30,.85) 40%, rgba(13,90,149,.55) 75%, rgba(134,198,232,0) 100%);
  }
  .contact-icon { left: 344px; width: 42px; height: 42px; }
  .icon-pin { top: 780px; }
  .icon-phone { top: 966px; }
  .icon-mail { top: 1032px; }
  .icon-web { top: 1092px; }
  .contact-text { left: 417px; font-weight: 700; color: var(--navy); line-height: 1; }
  .address { top: 782px; font-size: 27px; line-height: 45px; }
  .phone { top: 973px; font-size: 32px; }
  .email { top: 1037px; font-size: 27px; }
  .web { top: 1097px; font-size: 27px; left: 421px; }
</style>
</head>
<body>
<main class="flyer">
  <header class="brand">
    <div class="brand-name">HALSUM</div>
    <div class="brand-year">2019</div>
  </header>

  <h1 class="title">HARVEST LANTERN<br>SUMMIT</h1>

  <div class="date-label">DATE <span>-</span></div>
  <div class="date-lines">
    <div>AUGUST <span class="accent">8TH, 9TH, 10TH</span></div>
    <div class="second">AND <span class="accent">11TH, 2019</span></div>
  </div>

  <div class="start-time">START TIME&nbsp;<span class="accent">7:00PM</span></div>

  <div class="vision vision-prophetic">PROPHETIC</div>
  <div class="vision vision-overflow">OVERFLOW</div>
  <div class="vision vision-fire">FIRE</div>

  <div class="flame-area" role="img" aria-label="Large decorative flame in orange and deep blue rising from the lower left corner"></div>

  <svg class="contact-icon icon-pin" viewBox="0 0 42 56" aria-hidden="true">
    <path d="M21 2C10 2 3 10 3 19c0 12 18 35 18 35s18-23 18-35C39 10 32 2 21 2z" fill="var(--navy)"/>
    <circle cx="21" cy="19" r="6" fill="#e4f2f9"/>
  </svg>
  <div class="contact-text address">Talbot Community<br>Center (Downtown<br>Portland)482 Wexley<br>Street, Portland, ME</div>

  <svg class="contact-icon icon-phone" viewBox="0 0 42 42" aria-hidden="true">
    <rect width="42" height="42" rx="6" fill="var(--navy)"/>
    <path d="M13 9c2 0 3 4 4 6 0 2-3 3-2 5 2 4 4 6 7 7 2 1 3-2 5-2 2 1 6 2 6 4 0 3-3 5-6 5-10 0-19-9-19-19 0-3 2-6 5-6z" fill="#e4f2f9"/>
  </svg>
  <div class="contact-text phone">207 555 3184</div>

  <svg class="contact-icon icon-mail" viewBox="0 0 42 42" aria-hidden="true">
    <rect x="1" y="10" width="40" height="24" fill="none" stroke="var(--navy)" stroke-width="2.5"/>
    <path d="M1 10l20 14 20-14M1 34l15-12M41 34L26 22" fill="none" stroke="var(--navy)" stroke-width="2.5"/>
  </svg>
  <div class="contact-text email">contact@meadowcrest.org</div>

  <svg class="contact-icon icon-web" viewBox="0 0 42 42" aria-hidden="true">
    <g fill="none" stroke="var(--navy)" stroke-width="2.5">
      <circle cx="21" cy="21" r="19"/>
      <ellipse cx="21" cy="21" rx="8" ry="19"/>
      <path d="M2 21h38M5 11h32M5 31h32M21 2v38"/>
    </g>
  </svg>
  <div class="contact-text web">www.vostel.org</div>
</main>
</body>
</html>
```